Flyer for a 1 day conference event - with our design elements

We need a two sided A4 flyer created for our 1 day conference, using our corporate design elements.

It is an exclusive event for high profile professional speakers, and it's important for the flyer to be engaging, professional and clean.

We want the prospective attendees to see how much value there is in the day and to feel the event cannot be missed.

I will need to be able to make small edits back and forth with the successful designer in order to get it just-right. (ie: It won't work if I only get access to 2-3 revisions... but don't worry - I don't intend to request an entire re-design)

Target Market(s)

High profile professional speakers

Industry/Entity Type

Event

Requirements
Must have
• Not too much clutter. Some of own design elements
Nice to have
• A large image/photo. Doesnt have to be of a microphone or stage or curtain (traditional speaker things) .. it could be something 'spring' like because it being held in Spring.
Should not have
• too many colours. too many different fonts. too much clutter.

```html
<!DOCTYPE html>
<html lang="en">
<head>
<meta charset="utf-8">
<title>The MSP Unconvention</title>
<link rel="stylesheet" href="https://fonts.googleapis.com/css2?family=Oswald:wght@500;600&family=Open+Sans:wght@600&display=swap">
<style>
  :root {
    --navy: #1d3f7c;
    --band: #1f4d8f;
    --sky: #5aa9db;
    --sky-soft: #9ccbea;
    --sky-pale: #cfe6f5;
    --mist: #eef6fc;
    --plank: #d5dde6;
    --wood: #c9a77e;
    --grey: #8c9198;
    --white: #ffffff;
  }
  * { margin: 0; padding: 0; box-sizing: border-box; }
  html, body { width: 848px; height: 1200px; overflow: hidden; background: var(--white); }
  .flyer { position: relative; width: 848px; height: 1200px; overflow: hidden; background: var(--white); }
  .flyer > * { position: absolute; }
  .top-band { left: 0; top: 0; width: 848px; height: 220px; }
  .spring-scene {
    left: 0; top: 400px; width: 848px; height: 800px;
    background:
      radial-gradient(ellipse 150px 260px at 160px 480px, rgba(201,167,126,0.85) 0%, rgba(201,167,126,0.45) 55%, rgba(201,167,126,0) 100%),
      radial-gradient(ellipse 340px 420px at 150px 330px, var(--sky-soft) 0%, rgba(156,203,234,0.6) 45%, rgba(207,230,245,0) 85%),
      radial-gradient(ellipse 260px 300px at 420px 620px, rgba(156,203,234,0.55) 0%, rgba(207,230,245,0) 80%),
      radial-gradient(ellipse 260px 200px at 720px 420px, rgba(207,230,245,0.8) 0%, rgba(255,255,255,0) 80%),
      linear-gradient(180deg, rgba(255,255,255,0) 0%, rgba(255,255,255,0) 60%, var(--mist) 72%, var(--plank) 100%);
  }
  .brand {
    left: 64px; top: 40px; display: flex; align-items: center; gap: 14px;
    font-family: "Oswald", sans-serif; font-weight: 600; font-size: 26px; line-height: 1.05;
    color: var(--navy);
  }
  .brand-dot { width: 44px; height: 44px; border-radius: 50%; background: var(--sky); flex: none; }
  .event-copy { left: 0; top: 0; width: 848px; height: 1200px; }
  .event-copy text { font-family: "Oswald", sans-serif; font-weight: 600; }
  .tags text { font-family: "Open Sans", sans-serif; font-weight: 600; font-size: 24px; fill: var(--grey); }
  .tags circle { fill: var(--sky); }
  .dark { fill: var(--navy); }
  .light { fill: var(--sky); }
</style>
</head>
<body>
<main class="flyer">
  <svg class="top-band" viewBox="0 0 848 220" aria-hidden="true">
    <defs>
      <linearGradient id="bandPale" x1="0" y1="0" x2="1" y2="0">
        <stop offset="0" stop-color="#ffffff"/>
        <stop offset="1" stop-color="#bcdcf1"/>
      </linearGradient>
    </defs>
    <path d="M0 0 H848 V205 C700 150 520 100 320 78 C200 66 90 64 0 70 Z" fill="url(#bandPale)"/>
    <path d="M180 0 H848 V175 C690 110 500 62 300 32 C250 24 210 12 180 0 Z" fill="#8cc4e8"/>
    <path d="M230 0 H848 V150 C690 86 510 42 320 16 C285 10 255 5 230 0 Z" fill="var(--band)"/>
    <path d="M360 0 H848 V92 C720 46 560 16 360 0 Z" fill="#2b64a8"/>
  </svg>

  <div class="spring-scene" role="img" aria-label="Spring illustration: a wooden lectern with microphone on a pale plank stage, surrounded by soft blue floral swirls and butterflies"></div>

  <div class="brand">
    <span class="brand-dot"></span>
    <span>Speakers Guild<br>of Australasia</span>
  </div>

  <svg class="event-copy" viewBox="0 0 848 1200">
    <g class="tags">
      <text x="165" y="276" textLength="96" lengthAdjust="spacingAndGlyphs">No stars</text>
      <circle cx="276" cy="268" r="6"/>
      <text x="291" y="276" textLength="138" lengthAdjust="spacingAndGlyphs">No keynotes</text>
      <circle cx="444" cy="268" r="6"/>
      <text x="459" y="276" textLength="172" lengthAdjust="spacingAndGlyphs">No workshops</text>
      <circle cx="646" cy="268" r="6"/>
      <text x="661" y="276" textLength="155" lengthAdjust="spacingAndGlyphs">No tweets</text>
    </g>
    <text class="dark" x="165" y="346" font-size="80" textLength="651" lengthAdjust="spacingAndGlyphs">THE MSP UNCONVENTION</text>
    <text class="light" x="165" y="381" font-size="38" font-weight="500" textLength="651" lengthAdjust="spacingAndGlyphs">FOR EXPERIENCED, SUCCESSFUL SPEAKERS</text>
    <text class="dark" x="165" y="443" font-size="70" textLength="590" lengthAdjust="spacingAndGlyphs">8.30AM TILL</text>
    <text class="dark" transform="translate(816 443) rotate(-90)" font-size="60" textLength="52" lengthAdjust="spacingAndGlyphs">5PM</text>
    <text class="light" x="165" y="522" font-size="90" textLength="651" lengthAdjust="spacingAndGlyphs">NOVEMBER 5</text>
    <text class="dark" x="471" y="598" font-size="54" textLength="345" lengthAdjust="spacingAndGlyphs">PARKSIDE GRAND HOTEL</text>
    <text class="dark" transform="translate(490 653) rotate(-90)" font-size="24" textLength="38" lengthAdjust="spacingAndGlyphs">214</text>
    <text class="light" x="496" y="653" font-size="50" textLength="320" lengthAdjust="spacingAndGlyphs">GARDEN PDE</text>
    <text class="dark" x="471" y="710" font-size="54" textLength="345" lengthAdjust="spacingAndGlyphs">EAST BAYSIDE</text>
  </svg>
</main>
</body>
</html>
```